tallow brook systems ltd commercial solar installs

a bifold A4 brochure , explaining the benefits of solar panel and battery storage on commercial buildings in England

i dont have many images or paragraphs i was hoping that this could be part of your design

```html
<!DOCTYPE html>
<html lang="en">
<head>
<meta charset="utf-8">
<title>Tallow Brook Systems Ltd – Commercial Solar Installs Brochure</title>
<link href="https://fonts.googleapis.com/css2?family=Arimo:wght@400;700&display=swap" rel="stylesheet">
<style>
  :root{
    --green-bright:#6fee3b;
    --green-mid:#2fb52c;
    --green-deep:#168a1a;
    --green-ink:#0f4a12;
    --ink:#2b2b2b;
    --paper:#ffffff;
    --stage:#c9c9c9;
    --sky:#d9ecf7;
  }
  *{box-sizing:border-box;margin:0;padding:0}
  html,body{width:1200px;height:2738px;overflow:hidden;background:var(--stage)}
  body{position:relative;font-family:"Arimo",Arial,sans-serif;color:var(--ink)}

  .spread{position:absolute;left:87px;width:955px;height:738px;background:var(--paper);
    transform:scale(1.063);transform-origin:0 0;overflow:hidden;box-shadow:0 2px 6px rgba(0,0,0,.25)}
  .spread--outer{top:1060px}
  .spread--inner{top:1863px}
  .layer{position:absolute;left:0;top:0}
  .abs{position:absolute}

  /* ---------- outer: back panel ---------- */
  .brand-square{left:208px;top:463px;width:62px;height:60px;background:var(--green-mid);border-radius:6px}
  .brand-name{left:0;width:478px;top:533px;text-align:center;font-weight:700;font-size:21px;color:#333}
  .rule{height:3px;background:var(--green-ink);left:30px;width:423px}
  .rule--top{top:572px}.rule--bottom{top:685px}
  .cta{left:38px;width:240px;top:580px;text-align:center;font-weight:700;font-size:17px;line-height:21px;color:var(--green-ink)}
  .phone-pill{left:38px;top:626px;width:232px;height:42px;background:var(--green-bright);border:2px solid var(--green-ink);border-radius:5px}
  .phone-pill__icon{left:-2px;top:-2px;width:42px;height:42px;background:var(--green-ink);border-radius:5px 0 0 5px}
  .phone-pill__num{left:50px;top:5px;font-size:25px;font-weight:700;color:var(--green-ink);letter-spacing:.3px}
  .contact-divider{left:306px;top:606px;width:1px;height:62px;background:#555}
  .address{left:322px;top:606px;font-size:10.5px;line-height:12.5px;color:#333}
  .web{left:328px;top:652px;font-size:10.5px;color:#333}
  .icon-sm{position:absolute}
  .badges{left:150px;top:698px;display:flex;gap:14px;align-items:center}
  .badge{height:18px;border-radius:3px}
  .badge--a{width:60px;background:#f3d6d6}
  .badge--b{width:44px;background:#d7dff0}
  .badge--c{width:52px;height:28px;background:#e6d6ef}

  /* ---------- outer: front panel ---------- */
  .cover-title{left:478px;width:477px;top:588px;text-align:center;font-weight:700;font-size:41px;line-height:42px;color:var(--green-ink)}
  .cover-cta{left:478px;width:477px;top:684px;text-align:center;font-size:9px;font-weight:700;color:var(--green-ink)}
  .cover-pill{left:652px;top:697px;width:132px;height:23px;background:var(--green-bright);border:2px solid var(--green-ink);border-radius:12px}
  .cover-pill__icon{left:-2px;top:-2px;width:23px;height:23px;border-radius:50%;background:var(--green-ink)}
  .cover-pill__num{left:26px;top:2px;font-size:14px;font-weight:700;color:var(--green-ink)}

  /* ---------- inner ---------- */
  .inner-heading{left:35px;top:40px;color:#fff;font-weight:700;font-size:23.5px;line-height:29px}
  .section-tag{display:inline-block;background:var(--green-mid);border:2px solid var(--green-ink);color:#fff;font-weight:700;font-size:16px;line-height:20px;padding:0 5px;border-radius:2px}
  .col{position:absolute;font-size:8.1px;line-height:10.2px;color:var(--ink)}
  .col p{margin-bottom:8.5px;text-align:justify}
  .col--left{left:35px;top:135px;width:420px}
  .col--right{left:507px;top:170px;width:420px}
  .col .section-tag{margin:2px 0 6px}
  .pic{float:right;margin-left:10px}
  .pic--planet{width:128px;height:125px;margin-right:-23px;margin-top:-4px;background:#cfe9bd}
  .pic--money{width:102px;height:88px;margin-top:2px;margin-right:2px;background:#eee4d2}
  .clear{clear:both}
</style>
</head>
<body>

<!-- Outer spread: back panel + front cover -->
<section class="spread spread--outer">
  <svg class="layer" width="478" height="738" viewBox="0 0 478 738">
    <defs>
      <linearGradient id="evPhoto" x1="0" y1="0" x2="1" y2="1">
        <stop offset="0" stop-color="#e8e6e2"/><stop offset=".45" stop-color="#7a6a58"/><stop offset="1" stop-color="#3d3228"/>
      </linearGradient>
      <linearGradient id="swoosh" x1="0" y1="0" x2="1" y2="0">
        <stop offset="0" stop-color="#1f9e1f"/><stop offset=".6" stop-color="#3cc93a"/><stop offset="1" stop-color="#7ff04a"/>
      </linearGradient>
    </defs>
    <rect width="478" height="470" fill="url(#evPhoto)" role="img" aria-label="Photo of a man plugging a charging cable into a white electric car outside a timber house"/>
    <path d="M0,205 C150,238 330,370 478,435 L478,475 C320,405 150,318 0,300 Z" fill="url(#swoosh)"/>
    <path d="M0,262 C150,285 320,380 478,455 L478,470 C320,400 150,300 0,282 Z" fill="#a9f27a" opacity=".7"/>
    <path d="M0,300 C150,318 320,405 478,475 L478,738 L0,738 Z" fill="#fff"/>
  </svg>
  <svg class="layer" style="left:478px" width="477" height="738" viewBox="0 0 477 738">
    <defs>
      <linearGradient id="solarPhoto" x1="0" y1="0" x2="0" y2="1">
        <stop offset="0" stop-color="#5d6f86"/><stop offset=".5" stop-color="#2f4360"/><stop offset="1" stop-color="#6d7684"/>
      </linearGradient>
    </defs>
    <rect width="477" height="560" fill="url(#solarPhoto)" role="img" aria-label="Photo of an installer in hard hat and hi-vis vest climbing a ladder beside rows of solar panels"/>
    <path d="M0,418 C130,470 300,500 477,448 L477,478 C300,528 120,488 0,445 Z" fill="var(--green-deep)"/>
    <path d="M0,445 C120,488 300,528 477,478 L477,738 L0,738 Z" fill="var(--green-bright)"/>
  </svg>

  <div class="abs brand-square" aria-hidden="true"></div>
  <div class="abs brand-name">Tallow Brook Systems Ltd</div>
  <div class="abs rule rule--top"></div>
  <div class="abs cta">Talk To Us Today<br>Book A Home Visit</div>
  <div class="abs phone-pill">
    <div class="abs phone-pill__icon">
      <svg class="icon-sm" style="left:10px;top:10px" width="22" height="22" viewBox="0 0 24 24"><path fill="#fff" d="M6.6 10.8a15 15 0 006.6 6.6l2.2-2.2c.3-.3.7-.4 1-.2 1.1.4 2.3.6 3.6.6.6 0 1 .4 1 1V20c0 .6-.4 1-1 1A17 17 0 013 4c0-.6.4-1 1-1h3.5c.6 0 1 .4 1 1 0 1.3.2 2.5.6 3.6.1.3 0 .7-.2 1z"/></svg>
    </div>
    <div class="abs phone-pill__num">01632 480215</div>
  </div>
  <div class="abs contact-divider"></div>
  <svg class="abs" style="left:310px;top:607px" width="9" height="12" viewBox="0 0 24 32"><path fill="var(--green-mid)" d="M12 0C5.4 0 0 5.4 0 12c0 9 12 20 12 20s12-11 12-20C24 5.4 18.6 0 12 0zm0 17a5 5 0 110-10 5 5 0 010 10z"/></svg>
  <div class="abs address">7 Ferrow Trading Park<br>Alderbury Vale<br>Kent KV4 2QT</div>
  <svg class="abs" style="left:311px;top:653px" width="11" height="11" viewBox="0 0 24 24"><circle cx="12" cy="12" r="10" fill="none" stroke="var(--green-mid)" stroke-width="2.4"/><path d="M2 12h20M12 2c3 3 3 17 0 20M12 2c-3 3-3 17 0 20" fill="none" stroke="var(--green-mid)" stroke-width="2"/></svg>
  <div class="abs web">www.tallowbrooksystems.co</div>
  <div class="abs rule rule--bottom"></div>
  <div class="abs badges" aria-label="Partner badges">
    <div class="badge badge--a"></div><div class="badge badge--b"></div><div class="badge badge--c"></div>
  </div>

  <div class="abs cover-title">COMMERCIAL<br>SOLAR INSTALLS</div>
  <div class="abs cover-cta">TALK TO US TODAY BOOK A HOME VISIT</div>
  <div class="abs cover-pill">
    <div class="abs cover-pill__icon">
      <svg class="icon-sm" style="left:5px;top:5px" width="13" height="13" viewBox="0 0 24 24"><path fill="#fff" d="M6.6 10.8a15 15 0 006.6 6.6l2.2-2.2c.3-.3.7-.4 1-.2 1.1.4 2.3.6 3.6.6.6 0 1 .4 1 1V20c0 .6-.4 1-1 1A17 17 0 013 4c0-.6.4-1 1-1h3.5c.6 0 1 .4 1 1 0 1.3.2 2.5.6 3.6.1.3 0 .7-.2 1z"/></svg>
    </div>
    <div class="abs cover-pill__num">01632 480215</div>
  </div>
</section>

<!-- Inner spread -->
<section class="spread spread--inner">
  <svg class="layer" width="955" height="738" viewBox="0 0 955 738">
    <defs>
      <linearGradient id="header" x1="0" y1="0" x2="1" y2="0">
        <stop offset="0" stop-color="#159a17"/><stop offset=".55" stop-color="#28b526"/><stop offset="1" stop-color="#62e23a"/>
      </linearGradient>
      <linearGradient id="battery" x1="0" y1="0" x2="1" y2="1">
        <stop offset="0" stop-color="#1c4aa3"/><stop offset=".6" stop-color="#4f7fd0"/><stop offset="1" stop-color="#dce6f4"/>
      </linearGradient>
    </defs>
    <rect x="520" y="0" width="435" height="160" fill="var(--sky)" role="img" aria-label="Illustration of a modern house with rooftop solar panels and a red electric car charging in the garage"/>
    <path d="M0,0 L700,0 C610,90 520,135 330,132 C200,130 90,128 0,140 Z" fill="url(#header)"/>
    <path d="M330,132 C520,135 610,90 700,0 L716,0 C620,100 520,148 330,140 C200,136 90,136 0,146 L0,140 C90,128 200,130 330,132 Z" fill="#8ff05a"/>
    <rect x="478" y="586" width="477" height="152" fill="url(#battery)" role="img" aria-label="Illustration of a house built from green batteries with a solar panel roof"/>
  </svg>

  <div class="abs inner-heading">Why start using<br>TALLOW BROOK SYSTEMS TODAY?</div>

  <div class="col col--left">
    <span class="section-tag">Save the planet?</span>
    <p>Climate change is real and it's happening today. Our world will change irreparably if we do not change our way of living today. By reducing your own CO2 emissions and installing solar-powered energy systems then you are doing your bit to help save our planet from a climate disaster.</p>
    <p>The directors and employees at Tallow Brook Systems, have been installing solar power systems for over 15 years all across the southeast of England and have the experience necessary to complete even the most complex of installations.</p>
    <div class="pic pic--planet" role="img" aria-label="Illustration of two hands holding a green globe with the words save the planet"></div>
    <p>In truth, solar power can now be installed in under a day for most homes and is very affordable. Solar energy is the planet's most abundant, energy source available.</p>
    <p>There are two ways that solar technologies harness solar energy, Solar Photovoltaics and Solar Thermal. Solar Photovoltaic (or PV) is a technology that converts our sunlight into direct current electricity by using semiconductors. Alternatively, Solar Thermal is a technology which uses the heat and energy from the sun for heating or producing electricity.</p>
    <div class="clear"></div>
    <span class="section-tag">Save you money?</span>
    <p>Using solar power to produce your heating and electricity supply at home can fully repay your initial investment over time.</p>
    <p>Under the smart export guarantee (SEG) scheme which was launched in January 2020, households get paid for solar energy they 'export'. This is electricity you generate, but don't use yourself, which is then pumped back into the national energy grid.</p>
    <div class="pic pic--money" role="img" aria-label="Illustration of a hand holding banknotes"></div>
    <p>With electric prices at a record high and the predictions that they will continue to rise over the next few years, it's never been a better time to invest in solar power. Solar panels can last over 40 years so upgrading your energy delivery system today can enable you to lock into a much cheaper way to heat and power your home and avoid any large price hikes for the foreseeable future.</p>
    <p>Our solar energy, friendly team is on hand to help with your questions today, so feel free to get in touch on 01632 480215.</p>
    <div class="clear"></div>
    <p>Solar power can save you money today and even more in the future.</p>
    <span class="section-tag">Home Car Charging</span>
    <p>Tallow Brook Systems can install most electric car charging points at your home in just one day.</p>
    <p>Typically plug-in hybrids such as a Corvane charge at a rate of 3.7kW, and reach maximum charge in under 3 hours however fully electric cars such as a Halvard can charge at 7.4kW on a single-phase supply but have a much bigger battery. Typically it will take you up to 10 hours to charge a fully electric car. A 3.7kW charges at a rate of approximately 12mph, a 7.4kW will charge at a rate of approximately 24mph.</p>
    <p>Can my solar panels charge my electric car?</p>
  </div>

  <div class="col col--right">
    <p>Yes, there are a couple of ways to do this. One is to use the Voltmend charger or an equivalent that diverts excess power generation into an electric vehicle. This way, what would have been exported back to the grid is now providing you with zero-carbon footprint transport. Your electric car though must be parked at home during the daylight hours.</p>
    <p>The other alternative is to use a battery system to store this excess energy, and then discharge this into your EV in the evening. The battery would also cover your household electric requirements once the sunlight has disappeared for the day.</p>
    <p>As electric vehicles charge from an AC supply you cannot charge directly from solar so you will need an inverter to do this.</p>
    <span class="section-tag">Home Energy Storage</span>
    <p>Home battery storage is an innovative way for energy-conscious consumers to help the planet out with some extra energy. If you have solar panels installed on your house roof, there's a pretty clear benefit to storing any unused or unwanted electricity in a battery to use at night or days when the sun is not shining so brightly.</p>
    <p>Home battery storage for unused electricity isn't new though. Off-grid solar or photovoltaic (PV) and wind electricity generation on properties not connected to a power source have used battery storage to capture the unused electricity for many years, however, now that new technology is available, this energy can be stored quicker and cheaper than ever before.</p>
    <p>Storage batteries are increasingly popular with new solar installations, along with adding an EV car charging point. Tallow Brook Systems can provide you with a free quotation that includes all three installations, often all on the same day.</p>
    <p>If it's the money-saving aspect that appeals to you most or the fact that you are helping the planet to generate more energy from renewable sources or you just want to be off the grid, or all of the above, then installing solar panels, battery storage and EV car charging points in your home is definitely worth looking at.</p>
    <p>If your solar panel array and battery are large enough, you can run your home substantially on solar power. Using electricity from your battery can be cheaper per kilowatt-hour than using electricity from the grid, depending on the time of day and electricity tariffs in your area. Get in touch with Tallow Brook Systems to find out more and start making those savings today.</p>
  </div>
</section>

</body>
</html>
```